ZEPHIRO needs a new business card!

ZEPHIRO is a group of gaming enthusiasts who are looking for a new corporate business card.

The typeface should be modern and minimalist with attention paid to spacing between the letters and the letters 'zephiro' look relative to each other.

Should clean, crisp and minimalist - looking serious overall but with slight tweaks to the letters to make them look playful...

Black on white is fine.

Details on the card should include:
-the word 'zephiro'
-a job title (use any, for e.g. founder)
-a name (e.g. Ned Falka)
-phone number
-email address

For inspiration: http://brisket.tumblevane-cdn.example/wp-content/uploads/2013/07/mela-1.jpg

Target Market(s)

Video gaming enthusiasts

Industry/Entity Type

Business

Requirements
Must have
• Black letter on white background.
The word "zephiro"
Nice to have
• Maybe use a conservative font like Gibraltar or Helvetica and tweaking each letter individually.

You can insert normal job titles under the "zephiro" typeface
Should not have
• Should not be cartoony or childish fonts. No colors.

```html
<!DOCTYPE html>
<html lang="en">
<head>
<meta charset="UTF-8">
<title>ZEPHIRO Business Card</title>
<link href="https://fonts.googleapis.com/css2?family=Arimo:wght@400;700&display=swap" rel="stylesheet">
<style>
  :root {
    --backdrop-center: #ffffff;
    --backdrop-edge: #e4e5e7;
    --card-bg: #ffffff;
    --card-border: #dcdddf;
    --ink: #333333;
  }
  * { margin: 0; padding: 0; box-sizing: border-box; }
  html, body {
    width: 1200px;
    height: 1000px;
    overflow: hidden;
  }
  body {
    position: relative;
    background: radial-gradient(ellipse at center, var(--backdrop-center) 35%, var(--backdrop-edge) 100%);
    font-family: "Arimo", "Helvetica Neue", Arial, sans-serif;
    color: var(--ink);
  }
  .business-card {
    position: absolute;
    left: 82px;
    top: 176px;
    width: 1039px;
    height: 649px;
    background: var(--card-bg);
    border: 1px solid var(--card-border);
  }
  .brand-name {
    position: absolute;
    left: 0;
    right: 0;
    top: 170px;
    text-align: center;
    font-weight: 700;
    font-size: 150px;
    line-height: 1;
    letter-spacing: -6px;
    color: var(--ink);
  }
  .holder {
    position: absolute;
    left: 0;
    right: 0;
    top: 392px;
    text-align: center;
    font-weight: 400;
  }
  .holder-name {
    font-size: 30px;
    letter-spacing: 1.5px;
    line-height: 36px;
  }
  .holder-title {
    font-size: 25px;
    line-height: 36px;
    letter-spacing: 0.5px;
  }
  .contact {
    position: absolute;
    left: 0;
    right: 0;
    top: 507px;
    text-align: center;
    font-size: 25px;
    line-height: 36px;
    letter-spacing: 0.3px;
  }
</style>
</head>
<body>
  <main class="business-card">
    <h1 class="brand-name">zephiro</h1>
    <div class="holder">
      <p class="holder-name">NED FALKA</p>
      <p class="holder-title">Founder</p>
    </div>
    <div class="contact">
      <p class="contact-phone">Phone : +00 000 0000</p>
      <p class="contact-email">Email: nedfalka@quillmail.example</p>
    </div>
  </main>
</body>
</html>
```